Unique Flyer Project - www.plumorchardpanel.com.au

The purpose of this flyer is trying to get recipients to visit the website www.plumorchardpanel.com.au and sign up to the offer. I need it to be simple/to the point, eye catching and professional. I will post up a basic idea I have but feel free to put your own spin on it if you think you have great ideas to get people to visit the site, if not then just improve upon the quality of mine and make it look like a respected company.

I also think a red band or something that REALLY catches the eye highlighting one of the important aspects of the flyer (the domain?) could be great so even if someone is about to put it in the bin, the popping red-on-white-background catches their eye so they end up looking at and reading the flyer.

I would also love a VERY SIMPLE design for the backside of the flyer, just a red box/band (whatever you think is good) with the domain 'www.plumorchardpanel.com.au' in it. NOTHING ELSE! Just so if it's floating around the table and it's upside down, there's something eye catching that might entice the householder to look at it.

DESIGN IS FOR DL FLYER: 99mm X 210mm

Target Market(s)

Australian Residents interested in earning money from home.

Industry/Entity Type

It Company

Requirements
Must have
• Eye catching (mainly red band/box/bar on front & back page), SIMPLE, elegant/professional.
Should not have
• ANYTHING unnecessary to the reader that will distract them from the ultimate point - GET PAID TO DO SURVEYS FROM YOUR OWN HOME ON THE COMPUTER!

```html
<!DOCTYPE html>
<html lang="en">
<head>
<meta charset="utf-8">
<title>Plum Orchard Panel – DL Flyer, Front and Back</title>
<link rel="stylesheet" href="https://fonts.googleapis.com/css2?family=Anton&family=Roboto+Condensed:wght@700&display=swap">
<style>
  :root {
    --brand-red: #c8191f;
    --ink: #0d0d0d;
    --paper: #ffffff;
    --stage: #e6e6e6;
    --flyer-w: 300px;
    --flyer-h: 636px;
  }
  * { margin: 0; padding: 0; box-sizing: border-box; }
  html, body {
    width: 1200px;
    height: 750px;
    overflow: hidden;
    background: var(--stage);
  }
  .stage {
    width: 1200px;
    height: 750px;
    display: flex;
    align-items: center;
    justify-content: center;
    gap: 80px;
  }
  .flyer {
    position: relative;
    width: var(--flyer-w);
    height: var(--flyer-h);
    overflow: hidden;
    box-shadow: 0 6px 18px rgba(0, 0, 0, 0.18);
  }

  /* Front side */
  .flyer-front { background: var(--brand-red); }
  .front-top {
    height: 352px;
    background: var(--paper);
    padding: 30px 18px 0 22px;
  }
  .headline {
    font-family: "Anton", "Arial Narrow", sans-serif;
    font-weight: 400;
    text-transform: uppercase;
    color: var(--ink);
    font-size: 70px;
    line-height: 0.9;
    letter-spacing: -0.5px;
  }
  .headline .line { display: block; }
  .headline .accent { color: var(--brand-red); }
  .headline .big { font-size: 84px; }
  .tagline {
    margin-top: 8px;
    font-family: "Roboto Condensed", "Arial Narrow", sans-serif;
    font-weight: 700;
    font-size: 11px;
    letter-spacing: 0.2px;
    text-transform: uppercase;
    color: var(--brand-red);
  }
  .front-url {
    padding: 14px 22px 0;
    font-family: "Roboto Condensed", "Arial Narrow", sans-serif;
    font-weight: 700;
    font-size: 16px;
    color: var(--paper);
  }
  .scene-art {
    position: absolute;
    left: 0;
    bottom: 40px;
    width: 210px;
    height: 190px;
    background: linear-gradient(135deg, rgba(13,13,13,0.55) 0%, rgba(13,13,13,0.9) 70%);
  }

  /* Back side */
  .flyer-back { background: var(--brand-red); }
  .back-url {
    position: absolute;
    left: 50%;
    top: 50%;
    transform: translate(-50%, -50%) rotate(-90deg);
    white-space: nowrap;
    font-family: "Roboto Condensed", "Arial Narrow", sans-serif;
    font-weight: 700;
    font-size: 42px;
    letter-spacing: 0.3px;
    color: var(--paper);
  }
</style>
</head>
<body>
<main class="stage">
  <section class="flyer flyer-front" aria-label="Flyer front">
    <div class="front-top">
      <h1 class="headline">
        <span class="line">Get</span>
        <span class="line accent">Paid</span>
        <span class="line">To Do</span>
        <span class="line">Surveys</span>
      </h1>
      <p class="tagline">From your own home on the computer!</p>
    </div>
    <p class="front-url">www.plumorchardpanel.com.au</p>
    <div class="scene-art" role="img" aria-label="Black silhouette of a person relaxing in a reclined chair with a laptop, a drink raised beside them"></div>
  </section>

  <section class="flyer flyer-back" aria-label="Flyer back">
    <p class="back-url">www.plumorchardpanel.com.au</p>
  </section>
</main>
</body>
</html>
```